Carry The Tide Home

Business Card design

Target Market(s)

People who require support in the commnity

Industry/Entity Type

Mental Health Support

Contact Information for Business Card

Mental Health Support Rosalind Bratten carrythetidehome@mailvane.com.au 0481 637 592 PO Box 629 Tallowmere Bay 4871

Colors
6B429C
8869AF
B7A5CE
E3DAEB
F3F0F8

Requirements
Must have
• Logo & details listed above
Should not have
• No red or orange

```html
<!DOCTYPE html>
<html lang="en">
<head>
<meta charset="utf-8">
<title>Carry The Tide Home – Business Card</title>
<link rel="stylesheet" href="https://fonts.googleapis.com/css2?family=Open+Sans:wght@400;600&display=swap">
<style>
  :root {
    --stage: #2b2b2e;
    --card-dark: #1f1e22;
    --purple: #6b429c;
    --purple-mid: #8869af;
    --purple-light: #b7a5ce;
    --lavender: #e3daeb;
    --mist: #f3f0f8;
    --sun: #e6e12c;
    --text-light: #f3f0f8;
  }
  * { box-sizing: border-box; margin: 0; padding: 0; }
  html, body {
    width: 1200px; height: 780px; overflow: hidden;
    background: var(--stage);
    font-family: "Open Sans", Arial, sans-serif;
  }
  .canvas {
    position: relative; width: 1200px; height: 780px;
    display: flex; align-items: center; justify-content: center; gap: 40px;
  }
  .card {
    position: relative; width: 540px; height: 310px; flex: none;
    border-radius: 4px; overflow: hidden;
    box-shadow: 0 10px 28px rgba(0,0,0,.45);
  }

  /* Front: contact side */
  .card--front { background: var(--card-dark); color: var(--text-light); }
  .brand {
    position: absolute; left: 120px; top: 22px;
    display: flex; align-items: center; gap: 16px;
  }
  .brand__disc {
    width: 110px; height: 110px; border-radius: 50%; flex: none;
    background: var(--purple);
  }
  .brand__name {
    font-size: 15px; font-weight: 600; letter-spacing: .1em;
    text-transform: uppercase; color: var(--text-light);
  }
  .details {
    position: absolute; left: 26px; top: 146px;
    font-size: 16px; line-height: 21px;
  }
  .details__role, .details__name { display: block; }
  .contact { list-style: none; }
  .contact li { display: flex; align-items: center; gap: 8px; margin-left: -20px; }
  .contact svg { width: 13px; height: 13px; flex: none; }

  /* Back: pattern side */
  .card--back { background: var(--purple); }
  .back-pattern {
    position: absolute; inset: 0;
    background:
      radial-gradient(ellipse at 100% 40%, rgba(243,240,248,.55) 0%, rgba(183,165,206,.25) 30%, rgba(107,66,156,0) 60%),
      linear-gradient(135deg, #5f3a8f 0%, var(--purple) 50%, var(--purple-mid) 100%);
  }
  .back-brand {
    position: absolute; right: 60px; bottom: 42px;
    display: flex; align-items: center; gap: 9px;
  }
  .back-brand__disc {
    width: 14px; height: 14px; border-radius: 50%; background: var(--sun);
  }
  .back-brand__name {
    font-size: 11px; font-weight: 600; letter-spacing: .1em;
    text-transform: uppercase; color: var(--text-light);
  }
</style>
</head>
<body>
<main class="canvas">

  <section class="card card--front" aria-label="Business card front">
    <div class="brand">
      <span class="brand__disc"></span>
      <span class="brand__name">Carry The Tide Home</span>
    </div>
    <div class="details">
      <span class="details__role">Mental Health Support</span>
      <span class="details__name">Rosalind Bratten</span>
      <ul class="contact">
        <li>
          <svg viewBox="0 0 16 16" aria-hidden="true"><path d="M4 1.5l2.3 2.6-1.2 1.7c.9 2 2.4 3.5 4.4 4.4l1.7-1.2 2.6 2.3-1.3 2.2C7.6 13.3 2.7 8.4 1.8 3.3z" fill="var(--sun)"/></svg>
          <span>0481 637 592</span>
        </li>
        <li>
          <svg viewBox="0 0 16 16" aria-hidden="true"><rect x="1.5" y="3.5" width="13" height="9" rx="1" fill="none" stroke="var(--sun)" stroke-width="1.5"/><path d="M2 4.2l6 4.6 6-4.6" fill="none" stroke="var(--sun)" stroke-width="1.5"/></svg>
          <span>carrythetidehome@mailvane.com.au</span>
        </li>
        <li>
          <svg viewBox="0 0 16 16" aria-hidden="true"><path d="M8 1a4.6 4.6 0 0 0-4.6 4.6C3.4 9 8 14.5 8 14.5S12.6 9 12.6 5.6A4.6 4.6 0 0 0 8 1z" fill="var(--sun)"/><circle cx="8" cy="5.6" r="1.7" fill="var(--card-dark)"/></svg>
          <span>PO Box 629 Tallowmere Bay 4871</span>
        </li>
      </ul>
    </div>
  </section>

  <section class="card card--back" aria-label="Business card back">
    <div class="back-pattern" role="img" aria-label="Repeating star pattern in purple tones, brightening to pale sparkles at the right edge"></div>
    <div class="back-brand">
      <span class="back-brand__disc"></span>
      <span class="back-brand__name">Carry The Tide Home</span>
    </div>
  </section>

</main>
</body>
</html>
```